Business card for Quorvane, LLC

I need a business card template in .ai or similar format for my IT consultancy, Quorvane(.com)

Front side: The usual name/title/number/fax/email/contact info. Definitely san-serif, the logo font is MuseoSans 500 so the company name (Quorvane, LLC.) should definitely be in the same type and the rest of the text should be that or something complimentary. Including logo on the front is optional - I would prefer designs that include both with and without. I am open to creative input on the format.

Back side: Company logo framed somehow. I was thinking red background with the logo in a white circle in the middle, tho' I'm not sure how that would play off the red ball in the elephant's trunk. Open to creative input here too.

Attached are a (very rough) one-sided card mock-up I made, along with the logo and logo font.

```html
<!DOCTYPE html>
<html lang="en">
<head>
<meta charset="utf-8">
<title>Quorvane, LLC — Business Card</title>
<link href="https://fonts.googleapis.com/css2?family=Nunito+Sans:wght@400;600;800&display=swap" rel="stylesheet">
<style>
  :root {
    --brand-red: #e3232e;
    --brand-red-dark: #c81a24;
    --card-white: #f4f4f4;
    --ink-grey: #4a4a4c;
    --page-bg: #2b2b2d;
    --text-light: #ffffff;
  }
  * { margin: 0; padding: 0; box-sizing: border-box; }
  html, body {
    width: 1200px; height: 1024px; overflow: hidden;
    background: var(--page-bg);
    font-family: "Nunito Sans", Arial, sans-serif;
  }
  .sheet {
    position: relative; width: 1200px; height: 1024px;
    display: flex; flex-direction: column; align-items: center; justify-content: center; gap: 40px;
  }
  .card {
    position: relative; width: 840px; height: 460px; overflow: hidden;
    box-shadow: 0 10px 30px rgba(0,0,0,.45);
  }

  /* Back side */
  .card-back { background: var(--brand-red); }
  .card-back .brand-mark {
    position: absolute; left: 150px; top: 70px; width: 250px; height: 250px;
    border-radius: 50%; background: var(--ink-grey); opacity: .9;
  }
  .card-back .brand-name {
    position: absolute; right: 70px; top: 200px; text-align: right;
    color: var(--text-light); font-weight: 800; font-size: 64px; letter-spacing: 1px; line-height: 1;
  }
  .card-back .brand-name .domain { display: block; font-size: 22px; letter-spacing: 0; margin-top: 2px; }

  /* Front side */
  .card-front { background: var(--card-white); }
  .card-front .panel { position: absolute; inset: 0; }
  .card-front .logo-block { position: absolute; left: 70px; top: 120px; width: 320px; text-align: center; }
  .card-front .logo-circle {
    width: 150px; height: 150px; border-radius: 50%; background: var(--ink-grey);
    margin: 0 auto 26px;
  }
  .card-front .brand-name {
    color: var(--brand-red); font-weight: 800; font-size: 48px; letter-spacing: 1px; line-height: 1;
  }
  .person { position: absolute; left: 520px; top: 70px; color: var(--text-light); }
  .person .name { font-weight: 800; font-size: 34px; line-height: 1.1; }
  .person .title { font-weight: 600; font-size: 19px; }
  .address { position: absolute; left: 520px; top: 170px; color: var(--text-light); font-size: 19px; line-height: 1.3; }
  .contact-list {
    position: absolute; left: 520px; top: 272px; list-style: none;
    color: var(--text-light); font-size: 19px; line-height: 1.4;
  }
  .contact-icons { position: absolute; left: 455px; top: 275px; }
</style>
</head>
<body>
<main class="sheet">

  <section class="card card-back" aria-label="Card back">
    <div class="brand-mark" role="img" aria-label="Brand symbol area"></div>
    <div class="brand-name">QUORVANE<span class="domain">.com</span></div>
  </section>

  <section class="card card-front" aria-label="Card front">
    <svg class="panel" viewBox="0 0 840 460" width="840" height="460" aria-hidden="true">
      <path fill="var(--brand-red)"
        d="M440 0 H840 V460 H440 V385
           Q440 370 455 370 H488 Q503 370 503 355 V285 Q503 270 488 270 H455 Q440 270 440 255
           V130 L425 115 L440 100 Z"/>
    </svg>

    <div class="logo-block">
      <div class="logo-circle"></div>
      <div class="brand-name">QUORVANE</div>
    </div>

    <div class="person">
      <div class="name">Dalen Forsyth</div>
      <div class="title">Problem Eliminator</div>
    </div>
    <div class="address">18 Marlow Ct. Ashbury<br>PA 19380-4416</div>

    <svg class="contact-icons" width="40" height="100" viewBox="0 0 40 100" aria-hidden="true">
      <g fill="var(--brand-red)">
        <!-- phone -->
        <path d="M8 8 Q20 2 32 8 L30 13 L25 12 L24 9 Q20 8 16 9 L15 12 L10 13 Z"/>
        <rect x="12" y="14" width="16" height="7" rx="2"/>
        <!-- mobile -->
        <rect x="14" y="30" width="12" height="20" rx="2"/>
        <!-- fax -->
        <rect x="10" y="58" width="20" height="12" rx="2"/>
        <rect x="14" y="54" width="12" height="5"/>
        <!-- envelope -->
        <rect x="10" y="80" width="20" height="14" rx="1"/>
      </g>
      <path d="M10 81 L20 88 L30 81" stroke="var(--card-white)" stroke-width="1.6" fill="none"/>
      <rect x="16" y="33" width="8" height="12" fill="var(--card-white)"/>
    </svg>

    <ul class="contact-list">
      <li>1.800.555.0142</li>
      <li>1.610.555.0187</li>
      <li>1.610.555.0163</li>
      <li>dforsyth@quorvane.com</li>
    </ul>
  </section>

</main>
</body>
</html>
```